sommelier *

Sommelier Wine Hospitality Corvanne Star experience I'm working as a sommelier in a Corvanne Star restaurant. I try to reach People who are interested in invest in wine and wine loovers! In terms of color I would like to have a nice color based on a nice bordeaux red (as an advice). By the way i forgot to write my phone number and my email address. 439812604731 kdervin7@postiko.com I hope this info is enough so far.

```html
<!DOCTYPE html>
<html lang="en">
<head>
<meta charset="utf-8">
<title>Kasimir Dervin – Sommelier Business Card</title>
<link rel="stylesheet" href="https://fonts.googleapis.com/css2?family=Montserrat:wght@500;600;800&display=swap">
<style>
  :root {
    --backdrop: #5a5a5a;
    --card: #2b2a28;
    --bottle: #f0eeaa;
    --bordeaux: #d6203c;
    --ink: #2b2a28;
    --light-text: #ecebe6;
    --paint-red: #b3122a;
    --paint-yellow: #e9dc72;
    --paint-dark: #1f2236;
  }
  html, body {
    margin: 0;
    width: 1200px;
    height: 976px;
    overflow: hidden;
    background: var(--backdrop);
    font-family: "Montserrat", sans-serif;
  }
  .card {
    position: absolute;
    left: 100px;
    top: 202px;
    width: 1000px;
    height: 571px;
    background: var(--card);
    overflow: hidden;
    box-shadow: 0 20px 50px rgba(0,0,0,0.45);
  }
  .card-art { position: absolute; inset: 0; }
  .name-block {
    position: absolute;
    left: 360px;
    top: 172px;
  }
  .name {
    margin: 0;
    font-weight: 800;
    font-size: 44px;
    color: var(--ink);
    letter-spacing: 0.5px;
    line-height: 1;
  }
  .role {
    margin: 10px 0 0;
    font-weight: 600;
    font-size: 36px;
    color: var(--bordeaux);
    letter-spacing: 2.5px;
    line-height: 1;
  }
  .contact {
    position: absolute;
    left: 400px;
    top: 330px;
    margin: 0;
    padding: 0;
    list-style: none;
    color: var(--light-text);
    font-weight: 500;
    font-size: 24px;
  }
  .contact li {
    display: flex;
    align-items: center;
    gap: 16px;
    height: 40px;
  }
  .contact svg { width: 22px; height: 22px; }
  .tagline {
    position: absolute;
    right: 36px;
    bottom: 40px;
    margin: 0;
    color: var(--light-text);
    font-weight: 500;
    font-size: 20px;
    text-align: right;
    white-space: nowrap;
  }
</style>
</head>
<body>
  <div class="card">
    <svg class="card-art" viewBox="0 0 1000 571" width="1000" height="571">
      <defs>
        <linearGradient id="paintTones" x1="0" y1="0" x2="0" y2="1">
          <stop offset="0" stop-color="var(--paint-red)"/>
          <stop offset="0.35" stop-color="#c8323b"/>
          <stop offset="0.55" stop-color="var(--paint-yellow)"/>
          <stop offset="0.8" stop-color="#9b9a5a"/>
          <stop offset="1" stop-color="var(--paint-dark)"/>
        </linearGradient>
      </defs>
      <path class="paint-strip" role="img" aria-label="Abstract painted brushstrokes in wine red and yellow"
            fill="url(#paintTones)"
            d="M0 0 H40 C45 80 80 160 120 230 C170 300 200 360 195 420 C190 480 220 530 230 571 H0 Z"/>
      <path class="bottle" fill="var(--bottle)"
            d="M340 175 Q340 160 355 160 L375 160 L380 150 L620 150
               C660 150 680 90 700 0 L1000 0 L1000 330
               C880 330 720 280 640 290 L380 290 L375 282 L355 282
               Q340 282 340 268 Z"/>
    </svg>

    <div class="name-block">
      <h1 class="name">Kasimir Dervin</h1>
      <p class="role">Sommelier</p>
    </div>

    <ul class="contact">
      <li>
        <svg viewBox="0 0 24 24" aria-hidden="true"><path fill="var(--bordeaux)" d="M6.6 10.8a15 15 0 0 0 6.6 6.6l2.2-2.2a1 1 0 0 1 1-.25 11.4 11.4 0 0 0 3.6.6 1 1 0 0 1 1 1V20a1 1 0 0 1-1 1A17 17 0 0 1 3 4a1 1 0 0 1 1-1h3.5a1 1 0 0 1 1 1c0 1.25.2 2.45.6 3.6a1 1 0 0 1-.25 1z"/></svg>
        <span>+439812604731</span>
      </li>
      <li>
        <svg viewBox="0 0 24 24" aria-hidden="true"><rect x="2.5" y="5" width="19" height="14" fill="none" stroke="var(--bordeaux)" stroke-width="2"/><path d="M2.5 5 L12 13 L21.5 5 M2.5 19 L9.5 11.5 M21.5 19 L14.5 11.5" fill="none" stroke="var(--bordeaux)" stroke-width="2"/></svg>
        <span>kdervin7@postiko.com</span>
      </li>
    </ul>

    <p class="tagline">Sommelier • Wine • Hospitality • Corvanne Star Experience • Travel</p>
  </div>
</body>
</html>
```